Falcrest security business card

Looking for a business card for my security company

Target Market(s)

Security

Industry/Entity Type

Security

Contact Information for Business Card

Name - Gil Marston. Title - General manager - direct 314 862.4490 website www. falcrestsecurityservices.example email - gil@ falcrestsecurityservices.example

Requirements
Must have
• Logo attached

```html
<!DOCTYPE html>
<html lang="en">
<head>
<meta charset="utf-8">
<title>Falcrest Security Services – Business Card</title>
<link rel="stylesheet" href="https://fonts.googleapis.com/css2?family=Montserrat:wght@500;600&display=swap">
<style>
  :root {
    --page-bg: #181818;
    --card-top: #121212;
    --card-bottom: #040404;
    --gold: #b8893e;
    --gold-light: #f6f1d4;
    --white: #ffffff;
    --grey-1: #1c1c1c;
    --grey-2: #363636;
    --grey-3: #4f4f4f;
    --grey-4: #262626;
  }
  * { margin: 0; padding: 0; box-sizing: border-box; }
  html, body {
    width: 1171px;
    height: 1200px;
    overflow: hidden;
    background: var(--page-bg);
    font-family: "Montserrat", sans-serif;
  }
  .sheet {
    width: 1171px;
    height: 1200px;
    display: flex;
    flex-direction: column;
    align-items: center;
    justify-content: center;
    gap: 44px;
  }
  .card {
    display: block;
    width: 880px;
    height: 513px;
    box-shadow: 0 18px 40px rgba(0,0,0,0.45);
  }
  .brand-name { fill: var(--gold); font-weight: 600; letter-spacing: 1px; }
  .person-name { fill: var(--gold); font-weight: 600; font-size: 34px; letter-spacing: 1px; }
  .person-title { fill: var(--white); font-weight: 500; font-size: 20px; }
  .contact-text { fill: var(--white); font-weight: 500; font-size: 20px; }
  .icon { fill: var(--white); }
  .accent-stripe { fill: var(--gold); }
</style>
</head>
<body>
<main class="sheet">

  <!-- Front of card -->
  <svg class="card card-front" viewBox="0 0 816 476" xmlns="http://www.w3.org/2000/svg" aria-label="Business card front">
    <defs>
      <linearGradient id="card-fill" x1="0" y1="0" x2="0" y2="1">
        <stop offset="0" stop-color="var(--card-top)"/>
        <stop offset="1" stop-color="var(--card-bottom)"/>
      </linearGradient>
      <linearGradient id="gold-bar" x1="0" y1="0" x2="1" y2="0">
        <stop offset="0" stop-color="var(--gold)"/>
        <stop offset="0.35" stop-color="var(--gold)"/>
        <stop offset="1" stop-color="var(--gold-light)"/>
      </linearGradient>
    </defs>
    <rect class="card-base" width="816" height="476" fill="url(#card-fill)"/>

    <g class="corner-facets">
      <polygon points="560,476 816,40 816,476" fill="var(--grey-1)"/>
      <polygon points="612,476 816,118 816,476" fill="var(--grey-2)"/>
      <polygon points="727,476 816,320 816,476" fill="var(--grey-3)"/>
      <polygon points="772,476 816,400 816,476" fill="var(--grey-4)"/>
    </g>
    <polygon class="accent-stripe" points="547,476 561,476 697,262 683,262"/>

    <text class="person-name" x="43" y="82">GIL MARSTON</text>
    <text class="person-title" x="45" y="116">General Manager</text>

    <g class="brand-lockup">
      <text class="brand-name" x="623" y="98" font-size="46" text-anchor="middle">FALCREST</text>
    </g>

    <g class="contact-phone">
      <path class="icon" d="M50 350c2-2 5-2 6 0l3 4c1 2 0 4-1 5l-2 1c1 3 4 6 7 7l1-2c1-1 3-2 5-1l4 3c2 1 2 4 0 6l-2 2c-2 2-6 2-10 0-6-3-11-8-14-14-2-4-2-8 0-10z"/>
      <text class="contact-text" x="88" y="370">314 862.4490</text>
    </g>
    <g class="contact-web">
      <path class="icon" d="M48 392l24 7-10 3 7 9-3 2-7-9-5 8z"/>
      <text class="contact-text" x="93" y="403">www. falcrestsecurityservices.example</text>
    </g>

    <polygon class="gold-bar" points="0,463 368,463 380,476 0,476" fill="url(#gold-bar)"/>
  </svg>

  <!-- Back of card -->
  <svg class="card card-back" viewBox="0 0 816 476" xmlns="http://www.w3.org/2000/svg" aria-label="Business card back">
    <defs>
      <linearGradient id="card-fill-back" x1="0" y1="0" x2="0" y2="1">
        <stop offset="0" stop-color="var(--card-top)"/>
        <stop offset="1" stop-color="var(--card-bottom)"/>
      </linearGradient>
    </defs>
    <rect class="card-base" width="816" height="476" fill="url(#card-fill-back)"/>

    <g class="corner-facets">
      <polygon points="256,476 0,40 0,476" fill="var(--grey-1)"/>
      <polygon points="204,476 0,118 0,476" fill="var(--grey-2)"/>
      <polygon points="89,476 0,320 0,476" fill="var(--grey-3)"/>
      <polygon points="44,476 0,400 0,476" fill="var(--grey-4)"/>
    </g>
    <polygon class="accent-stripe" points="289,476 303,476 181,262 167,262"/>

    <g class="brand-lockup">
      <text class="brand-name" x="407" y="241" font-size="46" text-anchor="middle">FALCREST</text>
    </g>
  </svg>

</main>
</body>
</html>
```